I need a tradeshow booth designed

I need 2 graphics that compliment each other, here are the sizes:
Graphic Size: W119” x H92” Inches + W113” x H48” Inches (Case to Podium). Here are the details we would like to include on the booth. I will also show you a sample booth layout. Our website is www.lumbrafile.com
Records Management Services & Software
Spend time using your information instead of searching for it.
Torvane Record Partners
-Offers Records Management Software
-Document Scanning Services
-Document Storage
-Secure Shredding
Actively operating in over 1,000 school districts and career centers
Security
-SOC2 Compliant (this could be a graphic)
-HIPAA
-FERPA
Lumbrafile Software offers all of the following:
-Document Archive
-Electronic Forms & Workflows
-Record Request Public Portal
-Automated Records Retention
-Mileage & Expense Tracking
-Credit Card Payments
-Timesheets Management
-Electronic Signature
-Applicant Tracking
-HR Onboarding
-HR Information System
-Professional Development
-Substitute Management
Include a QR Code that goes to www.lumbrafile.com

```html
<!DOCTYPE html>
<html lang="en">
<head>
<meta charset="utf-8">
<title>Lumbrafile Tradeshow Graphics</title>
<link href="https://fonts.googleapis.com/css2?family=Poppins:ital,wght@0,400;0,500;0,600;0,700;0,800;1,700&display=swap" rel="stylesheet">
<style>
  :root {
    --red: #8a1518;
    --blue: #0a9fdc;
    --blue-deep: #1f6fc4;
    --sky: #cfeaf8;
    --ink: #1b1b1b;
    --page: #e8edf1;
  }
  * { box-sizing: border-box; margin: 0; padding: 0; }
  html, body { width: 750px; height: 1200px; overflow: hidden; }
  body { background: var(--page); font-family: "Poppins", sans-serif; color: var(--ink); position: relative; }

  .backwall {
    position: absolute; left: 30px; top: 150px; width: 690px; height: 534px;
    background: linear-gradient(160deg, #e4f1fa 0%, #ffffff 45%, #eaf5fc 100%);
    overflow: hidden; box-shadow: 0 4px 12px rgba(0,0,0,.15);
  }
  .backwall .top-band { position: absolute; left: 134px; top: 0; width: 422px; height: 6px; background: var(--blue); }
  .pattern {
    position: absolute;
    background: linear-gradient(315deg, #1f6fc4 0%, #2fb6ec 30%, #8fd6f5 55%, rgba(200,232,250,0) 80%);
  }
  .backwall .pattern { right: 0; bottom: 0; width: 360px; height: 260px; clip-path: polygon(100% 0, 100% 100%, 0 100%); }

  .brand-word { position: absolute; font-weight: 800; color: var(--red); letter-spacing: -1px; }
  .backwall .brand-word { left: 57px; top: 40px; font-size: 48px; line-height: 1; }

  .offers-title { position: absolute; left: 57px; top: 128px; font-size: 15px; font-weight: 700; line-height: 1.2; text-transform: uppercase; }
  .offers-title span { color: var(--red); }

  .feature-list { position: absolute; left: 57px; top: 175px; width: 256px; list-style: none; }
  .feature-list li { position: relative; height: 20px; margin-bottom: 5px; display: flex; align-items: center; }
  .feature-list .num {
    width: 22px; height: 20px; border-radius: 10px; font-size: 10px; font-weight: 600;
    display: flex; align-items: center; justify-content: center; z-index: 1;
  }
  .feature-list .bar {
    position: absolute; left: 14px; right: 0; top: 0; height: 20px; border-radius: 0 10px 10px 10px;
    padding-left: 28px; font-size: 10px; font-weight: 600; display: flex; align-items: center; text-transform: uppercase;
  }
  .feature-list li:nth-child(odd) .num { background: var(--red); color: #fff; border: 2px solid #fff; }
  .feature-list li:nth-child(odd) .bar { background: var(--red); color: #fff; }
  .feature-list li:nth-child(even) .num { background: var(--sky); color: var(--ink); }
  .feature-list li:nth-child(even) .bar { background: var(--sky); color: var(--ink); }

  .headline { position: absolute; left: 361px; top: 42px; font-size: 25px; font-weight: 800; color: var(--blue); line-height: 1.15; letter-spacing: -.2px; }
  .tagline { position: absolute; left: 361px; top: 108px; width: 282px; font-size: 13px; font-weight: 500; color: var(--blue); line-height: 1.3; }
  .tagline em { color: var(--red); font-weight: 700; }
  .rule { position: absolute; left: 361px; width: 276px; height: 1px; background: var(--blue); }

  .security-badge { position: absolute; left: 384px; top: 166px; width: 62px; text-align: center; }
  .security-badge svg { display: block; margin: 0 auto; }
  .security-badge .badge-label { font-size: 14px; font-weight: 800; color: var(--blue); line-height: 1; margin-top: 3px; }
  .security { position: absolute; left: 472px; top: 170px; }
  .security .label { font-size: 10px; font-weight: 700; text-transform: uppercase; }
  .security .label span { color: var(--red); }
  .security .item { display: flex; align-items: center; gap: 4px; font-size: 34px; font-weight: 700; line-height: 1; margin-top: 2px; }

  .partner-title { position: absolute; left: 361px; top: 280px; font-size: 13px; font-weight: 700; color: var(--red); }
  .partner-list { position: absolute; left: 361px; top: 299px; list-style: none; }
  .partner-list li { display: flex; align-items: center; gap: 7px; font-size: 12px; line-height: 16.3px; }
  .reach { position: absolute; left: 361px; top: 371px; width: 290px; font-size: 12.5px; font-weight: 700; line-height: 1.3; }
  .reach span { color: var(--blue); }

  .partner-mark { position: absolute; display: flex; align-items: center; gap: 8px; color: var(--red); font-weight: 700; }
  .partner-mark .sq { width: 18px; height: 18px; background: var(--red); flex: none; }
  .backwall .partner-mark { left: 361px; top: 430px; font-size: 20px; }

  .podium {
    position: absolute; left: 55px; top: 730px; width: 640px; height: 272px;
    background: #fff; overflow: hidden; box-shadow: 0 4px 12px rgba(0,0,0,.15);
  }
  .podium .pattern-left { left: 0; top: 0; width: 180px; height: 272px; clip-path: polygon(0 0, 100% 0, 0 100%);
    background: linear-gradient(135deg, #1f6fc4 0%, #2fb6ec 35%, #9ad9f5 70%, rgba(220,240,252,0) 100%); }
  .podium .pattern-right { right: 0; bottom: 0; width: 460px; height: 272px; clip-path: polygon(100% 0, 100% 100%, 0 100%); }
  .podium .partner-mark { left: 0; right: 0; top: 78px; justify-content: center; font-size: 22px; }
  .podium .subtitle { position: absolute; left: 0; right: 0; top: 140px; text-align: center; font-size: 14px; font-weight: 800; color: var(--blue); line-height: 1.15; }
  .podium .brand-word { left: 62px; top: 196px; font-size: 26px; }
</style>
</head>
<body>

<section class="backwall">
  <div class="top-band"></div>
  <div class="pattern" role="img" aria-label="Blue geometric triangle pattern"></div>

  <div class="brand-word">Lumbrafile</div>

  <h2 class="offers-title"><span>Lumbrafile</span> Software offers all<br>of the following:</h2>
  <ol class="feature-list">
    <li><span class="num">1</span><span class="bar">Document Archive</span></li>
    <li><span class="num">2</span><span class="bar">Electronic Forms &amp; Workflows</span></li>
    <li><span class="num">3</span><span class="bar">Record Request Public Portal</span></li>
    <li><span class="num">4</span><span class="bar">Automated Records Retention</span></li>
    <li><span class="num">5</span><span class="bar">Mileage &amp; Expense Tracking</span></li>
    <li><span class="num">6</span><span class="bar">Credit Card Payments</span></li>
    <li><span class="num">7</span><span class="bar">Timesheets Management</span></li>
    <li><span class="num">8</span><span class="bar">Electronic Signature</span></li>
    <li><span class="num">9</span><span class="bar">Applicant Tracking</span></li>
    <li><span class="num">10</span><span class="bar">HR Onboarding</span></li>
    <li><span class="num">11</span><span class="bar">HR Information System</span></li>
    <li><span class="num">12</span><span class="bar">Professional Development</span></li>
    <li><span class="num">13</span><span class="bar">Substitute Management</span></li>
  </ol>

  <h1 class="headline">Records Management<br>Services &amp; Software</h1>
  <p class="tagline">Spend time <em>using</em> your information instead of <em>searching</em> for it.</p>
  <div class="rule" style="top:152px"></div>

  <div class="security-badge">
    <svg width="54" height="64" viewBox="0 0 68 80" role="img" aria-label="SOC 2 compliance badge">
      <path d="M34 3 L64 12 V40 C64 60 48 72 34 78 C20 72 4 60 4 40 V12 Z" fill="#2aa6de" stroke="#1577b8" stroke-width="3"/>
      <path d="M34 11 L57 18 V40 C57 56 45 66 34 70 C23 66 11 56 11 40 V18 Z" fill="none" stroke="#fff" stroke-width="2"/>
    </svg>
    <div class="badge-label">SOC 2</div>
  </div>
  <div class="security">
    <div class="label">Torvane <span>Record Partners</span></div>
    <div class="item">
      <svg width="18" height="18" viewBox="0 0 18 18"><circle cx="9" cy="9" r="9" fill="#8a1518"/><path d="M5 9.5 L8 12 L13 6" fill="none" stroke="#fff" stroke-width="2.2"/></svg>HIPAA
    </div>
    <div class="item">
      <svg width="18" height="18" viewBox="0 0 18 18"><circle cx="9" cy="9" r="9" fill="#8a1518"/><path d="M5 9.5 L8 12 L13 6" fill="none" stroke="#fff" stroke-width="2.2"/></svg>FERPA
    </div>
  </div>
  <div class="rule" style="top:263px"></div>

  <h3 class="partner-title">Torvane Record Partners</h3>
  <ul class="partner-list">
    <li><svg width="9" height="9" viewBox="0 0 18 18"><circle cx="9" cy="9" r="9" fill="#8a1518"/><path d="M5 9.5 L8 12 L13 6" fill="none" stroke="#fff" stroke-width="2.5"/></svg>Offers Records Management Software</li>
    <li><svg width="9" height="9" viewBox="0 0 18 18"><circle cx="9" cy="9" r="9" fill="#8a1518"/><path d="M5 9.5 L8 12 L13 6" fill="none" stroke="#fff" stroke-width="2.5"/></svg>Document Scanning Services</li>
    <li><svg width="9" height="9" viewBox="0 0 18 18"><circle cx="9" cy="9" r="9" fill="#8a1518"/><path d="M5 9.5 L8 12 L13 6" fill="none" stroke="#fff" stroke-width="2.5"/></svg>Document Storage</li>
    <li><svg width="9" height="9" viewBox="0 0 18 18"><circle cx="9" cy="9" r="9" fill="#8a1518"/><path d="M5 9.5 L8 12 L13 6" fill="none" stroke="#fff" stroke-width="2.5"/></svg>Secure Shredding</li>
  </ul>
  <p class="reach">Actively operating in over <span>1,000</span> school districts and career centers</p>

  <div class="partner-mark"><span class="sq"></span>Torvane Record Partners</div>
</section>

<section class="podium">
  <div class="pattern pattern-left" role="img" aria-label="Blue geometric triangle pattern"></div>
  <div class="pattern pattern-right" role="img" aria-label="Blue geometric triangle pattern"></div>
  <div class="partner-mark"><span class="sq"></span>Torvane Record Partners</div>
  <p class="subtitle">Records Management<br>Services &amp; Software</p>
  <div class="brand-word">Lumbrafile</div>
</section>

</body>
</html>
```